Business card New design- upscale

Looking for modern design business cards. Minimalist, mix of gloss and matte finishes. Texas based Contractor company doing Mechanical hvac and plumbing, focused on commercial and industrial manufacturing facilities. We don't hand too many out so high end materials or functionality...will be considered. Please see attached files for info needed on cards. *New plumbing license needs to be edited to say K82917. Www.valtrimgroup.com
P.s. Website will also be redesigned soon.

Target Market(s)

Facility managers for commercial buildings, mechanical engineers for industrial manufacturing facilities including pharmaceutical, semiconductor, food & beverage, etc

Contact Information for Business Card

See attached images

Requirements
Must have
• All Logo colors: purple, black and Gray. 1, 2 or 4 rounded corners. All content on existing business cards (see attached images).
Nice to have
• Matte and gloss print. Embossing, raised print, functionality.
Should not have
• Stock images, generic construction.

```html
<!DOCTYPE html>
<html lang="en">
<head>
<meta charset="utf-8">
<title>Valtrim Group — Business Card</title>
<link href="https://fonts.googleapis.com/css2?family=Oswald:wght@500;600&family=Saira:wght@400;500;600&display=swap" rel="stylesheet">
<style>
  :root {
    --bg: #ece4da;
    --card: #f7f7f6;
    --purple: #3b2068;
    --purple-soft: #6d5a91;
    --gray: #5a5a5a;
    --dark-gray: #6b6b6b;
  }
  * { margin: 0; padding: 0; box-sizing: border-box; }
  html, body { width: 1200px; height: 974px; overflow: hidden; }
  body {
    background: var(--bg);
    display: flex;
    align-items: center;
    justify-content: center;
    gap: 70px;
    font-family: "Saira", sans-serif;
  }
  .card {
    width: 440px;
    height: 770px;
    background: var(--card);
    border-radius: 6px;
    box-shadow: 0 6px 18px rgba(80, 60, 40, 0.18);
    padding: 16px;
  }
  .card-frame {
    width: 100%;
    height: 100%;
    border: 2px solid var(--purple);
    display: flex;
    flex-direction: column;
    align-items: center;
    text-align: center;
  }
  /* Front */
  .front .card-frame { padding-top: 210px; }
  .brand {
    display: flex;
    align-items: center;
    gap: 12px;
    color: var(--purple);
    font-weight: 600;
    font-size: 38px;
    letter-spacing: 3px;
    line-height: 1;
  }
  .brand-mark { width: 26px; height: 26px; background: var(--purple); }
  .person-name {
    margin-top: 46px;
    font-family: "Oswald", sans-serif;
    font-weight: 600;
    font-size: 36px;
    color: var(--purple);
    line-height: 1;
  }
  .person-title { margin-top: 6px; font-size: 17px; color: #333; }
  .address, .contact {
    margin-top: 22px;
    font-size: 18px;
    color: var(--gray);
    line-height: 1.3;
  }
  .contact { margin-top: 18px; }
  .contact .web-line { font-size: 16px; }
  .divider {
    width: 76%;
    height: 1px;
    background: var(--purple-soft);
    margin-top: 24px;
  }
  .services {
    margin-top: 20px;
    font-size: 19px;
    font-style: italic;
    color: var(--purple);
    line-height: 1.25;
  }
  /* Back */
  .back .card-frame { padding-top: 200px; }
  .license-title {
    font-family: "Oswald", sans-serif;
    font-weight: 600;
    font-size: 25px;
    color: var(--dark-gray);
    line-height: 1.1;
  }
  .license-body {
    font-size: 18px;
    color: var(--gray);
    line-height: 1.3;
    padding: 4px 36px 0;
  }
  .license-phone {
    font-family: "Oswald", sans-serif;
    font-weight: 600;
    font-size: 25px;
    color: var(--purple);
    line-height: 1.3;
  }
  .license-block + .license-block { margin-top: 16px; }
  .license-web {
    margin-top: 8px;
    font-family: "Oswald", sans-serif;
    font-weight: 600;
    font-size: 22px;
    color: var(--purple);
    text-transform: uppercase;
  }
</style>
</head>
<body>
  <section class="card front">
    <div class="card-frame">
      <div class="brand"><span class="brand-mark"></span>VALTRIM GROUP</div>
      <h1 class="person-name">DANE HARLOW</h1>
      <p class="person-title">Lead Estimator/ sr. Project Manager</p>
      <p class="address">2186 Cedar Mill Rd.<br>Fort Worth, TX 76119</p>
      <p class="contact">
        P. (817) 555-0142<br>
        C. (520) 555-0178<br>
        <span class="web-line">dharlow@valtrimgroup.com</span><br>
        <span class="web-line">Www.valtrimgroup.com</span>
      </p>
      <div class="divider"></div>
      <p class="services">Commercial &amp; industrial Contractors<br>Mechanical &amp; Plumbing Services</p>
    </div>
  </section>

  <section class="card back">
    <div class="card-frame">
      <div class="license-block">
        <h2 class="license-title">PLUMBING LICENSE K82917</h2>
        <p class="license-body">Reulated by the Lone Star Board of Pipe Trade Examiners, P.o Box 3100, Austin TX 78765</p>
        <p class="license-phone">1-800-555-0163 | 512-555-0120</p>
      </div>
      <div class="license-block">
        <h2 class="license-title">TACLA31582C</h2>
        <p class="license-body">Regulater by the Lone Star Department of Trade Licensing P.O.Box 14520, Austin, TX.78714</p>
        <p class="license-phone">1-800-555-0191 | 512-555-0147</p>
        <p class="license-web">www.tradelicense-lonestar.org</p>
      </div>
    </div>
  </section>
</body>
</html>
```